Dravel

We are openıng one huntıng showroom in Riyadh? Saudi Arabia. Company name is "DRAVEL".
Our logo designed and we need Business Card Design now.
I attached DRAVEL logo below.
Front side will English and back side will be Arabic

```html
<!DOCTYPE html>
<html lang="en">
<head>
<meta charset="utf-8">
<title>Dravel – Business Card</title>
<link rel="stylesheet" href="https://fonts.googleapis.com/css2?family=Cairo:wght@700&family=Exo+2:wght@700&family=Lato:wght@400&display=swap">
<style>
  :root {
    --stage: #1c1c1c;
    --paper: #ffffff;
    --brand-green: #0b7a3e;
    --leaf-green: #6f9a3b;
    --ink: #1f1f1f;
    --rule: #d9d9d9;
  }
  * { margin: 0; padding: 0; box-sizing: border-box; }
  html, body {
    width: 1200px; height: 900px; overflow: hidden;
    background: var(--stage);
  }
  .stage { position: relative; width: 1200px; height: 900px; }

  .card {
    position: absolute;
    top: 275px;
    width: 477px;
    height: 293px;
    box-shadow: 4px 5px 8px rgba(0,0,0,0.55);
  }
  .card--front {
    left: 120px;
    background: var(--paper);
    border-radius: 0 62px 0 62px;
  }
  .card--back {
    left: 620px;
    background: var(--leaf-green);
    border-radius: 62px 0 62px 0;
  }

  .brand-name {
    position: absolute;
    font-family: "Exo 2", sans-serif;
    font-weight: 700;
    letter-spacing: 1px;
    line-height: 1;
  }
  .card--front .brand-name {
    left: 30px; top: 108px;
    font-size: 48px;
    color: var(--brand-green);
  }
  .brand-name--arabic {
    left: 0; right: 0; top: 112px;
    text-align: center;
    font-family: "Cairo", sans-serif;
    font-size: 66px;
    letter-spacing: 0;
    color: var(--paper);
  }

  .divider {
    position: absolute;
    left: 247px; top: 85px;
    width: 1px; height: 124px;
    background: var(--rule);
  }

  .contact {
    position: absolute;
    left: 268px; top: 83px;
    font-family: "Lato", sans-serif;
    font-size: 13.5px;
    color: var(--ink);
    line-height: 1;
  }
  .contact__name {
    font-family: "Exo 2", sans-serif;
    font-weight: 700;
    font-size: 18px;
    color: var(--brand-green);
    margin-left: 3px;
    letter-spacing: 0.3px;
  }
  .contact__role { margin-top: 1px; }
  .contact__list { list-style: none; margin-top: 5px; }
  .contact__list li {
    display: flex; align-items: center; gap: 4px;
    height: 18px;
  }
  .contact__list svg { width: 10px; height: 10px; fill: var(--brand-green); flex: none; }
  .contact__address { margin-top: 5px; line-height: 17px; }
</style>
</head>
<body>
<main class="stage">
  <section class="card card--front" aria-label="Card front">
    <div class="brand-name">DRAVEL</div>
    <div class="divider"></div>
    <div class="contact">
      <div class="contact__name">MARCUS HALE</div>
      <div class="contact__role">Managing Director</div>
      <ul class="contact__list">
        <li>
          <svg viewBox="0 0 10 10" aria-hidden="true"><path d="M1 3.2C1 2 2.2 1.2 5 1.2S9 2 9 3.2v.8H7V3H3v1H1z M2.3 4.4h5.4L9 8.6H1z"/></svg>
          055-210 734 618
        </li>
        <li>
          <svg viewBox="0 0 10 10" aria-hidden="true"><path d="M1 2h8v.6L5 5.2 1 2.6z M1 3.6l4 2.6 4-2.6V8H1z"/></svg>
          info@dravelhunt.com
        </li>
        <li>
          <svg viewBox="0 0 10 10" aria-hidden="true"><circle cx="5" cy="5" r="4.3"/></svg>
          www.dravelhunt.com
        </li>
      </ul>
      <div class="contact__address">88, Olaya Street<br>Riyadh, 12241</div>
    </div>
  </section>

  <section class="card card--back" aria-label="Card back" lang="ar" dir="rtl">
    <div class="brand-name brand-name--arabic">درافل</div>
  </section>
</main>
</body>
</html>
```